Webdesign für Importeur von Tierbedarfsartikeln
Zielgruppe
Wir importieren Tierbedarfsartikel und verkaufen sie ausschließlich online. Zielgruppe sind in erster Linie Katzenhalter.
Aufgabenstellung
Es gibt eine bestehende Webseite www.pfotenhain24.de Sie wurde bei Webrono erstellt und ist aktiv. Die Seite soll eine professionelle Ansicht erhalten. Schön wären edle Farben, nicht kunterbunt. Wichtig in dem Zusammenhang ist eben, dass sich derjenige mit dem Webronokonzept auskennt.
Dieser Auftrag wird Folgeaufträge erhalten, sprich Logo, Werbeflyer usw. Bilder der Produkte sind vorhanden.

```html
<!DOCTYPE html>
<html lang="de">
<head>
<meta charset="utf-8">
<title>Pfotenhain24 – Katzenbedarf online</title>
<link rel="stylesheet" href="https://fonts.googleapis.com/css2?family=Exo+2:wght@600;700&family=Open+Sans:wght@400;600&display=swap">
<style>
:root{
  --navy:#13239c;
  --blue-deep:#3a5cf4;
  --blue-sky:#5aaef5;
  --blue-link:#4ba0e6;
  --ink:#0b1450;
  --tan:#d8a36f;
  --pale:#e7f2fc;
  --text:#222;
  --white:#fff;
  --green:#8fd07c;
  --chip:#f1f1f1;
}
*{box-sizing:border-box;margin:0;padding:0}
html,body{width:1200px;height:2616px;overflow:hidden}
body{font-family:"Open Sans",sans-serif;color:var(--text);background:var(--white);font-size:13px}
.topbar{height:28px;background:var(--navy);color:var(--white);font-size:11px;display:flex;justify-content:center;align-items:center;gap:28px}
.topbar span{display:flex;align-items:center;gap:8px}
.header{height:104px;background:linear-gradient(90deg,var(--blue-deep),var(--blue-sky));position:relative}
.brand{position:absolute;left:226px;top:58px;display:flex;align-items:center;gap:8px;color:var(--white);font-size:24px;font-weight:600}
.brand i{width:16px;height:16px;border-radius:50%;background:var(--white);display:block}
.search{position:absolute;left:491px;top:37px;width:376px;height:28px;background:var(--white);border:1px solid #cfd8ee;color:var(--blue-deep);font-size:13px;padding:5px 9px}
.icons{position:absolute;left:898px;top:36px;display:flex;gap:12px}
.badge{position:absolute;left:52px;top:-4px;width:24px;height:24px;border-radius:50%;background:var(--ink);color:var(--white);font-size:12px;font-weight:600;display:flex;align-items:center;justify-content:center}
.nav{height:35px;background:var(--tan);display:flex;gap:23px;padding-left:223px;align-items:center;color:var(--white);font-size:12px;font-weight:600}
.hero{height:438px;background:linear-gradient(90deg,#e9e4dc 0%,#d9b48c 35%,#d88d43 50%,#dcc6a6 65%,#7a8a60 85%,#4a4a44 100%);position:relative}
.dots{position:absolute;left:563px;top:413px;display:flex;gap:8px}
.dots i{width:12px;height:12px;border-radius:50%;background:#d0d0d0;display:block}
.dots i:first-child{background:#2547f0}
.welcome{height:255px;background:var(--blue-sky);position:relative}
.welcome svg{position:absolute;left:289px;top:68px}
.welcome h1{position:absolute;left:433px;top:58px;font-family:"Exo 2",sans-serif;font-size:28px;color:var(--ink);font-weight:700}
.welcome p{position:absolute;left:433px;top:110px;width:490px;color:var(--white);font-size:13px;line-height:21px}
h2{font-family:"Exo 2",sans-serif;font-weight:700;font-size:27px;color:var(--blue-sky);text-align:center}
.offers{padding-top:42px;height:405px}
.offer-row{display:flex;gap:23px;margin:32px 0 0 223px}
.offer{width:171px;text-align:center}
.ph{display:block;width:171px;height:171px}
.title{color:var(--blue-link);font-size:13px;line-height:17px;margin-top:18px;min-height:34px}
.price{font-size:13px;margin-top:8px}
.stock{font-size:12px;margin-top:3px}
.opt{color:var(--blue-link)}
.rule{width:752px;height:1px;background:var(--blue-link);margin-left:223px}
.cats{padding-top:36px;height:384px}
.cat-row{display:flex;gap:47px;margin:37px 0 0 223px}
.cat{width:220px;height:222px;position:relative}
.cat span{position:absolute;left:50%;bottom:24px;transform:translateX(-50%);background:var(--blue-sky);color:var(--white);font-family:"Exo 2",sans-serif;font-weight:600;font-size:18px;padding:4px 12px;white-space:nowrap}
.sellers{background:var(--pale);height:794px;padding-top:46px}
.seller-grid{display:grid;grid-template-columns:repeat(3,220px);column-gap:47px;row-gap:23px;margin:31px 0 0 223px}
.seller{background:var(--white);height:298px;padding:26px 23px 0;text-align:center;box-shadow:0 1px 3px rgba(0,0,0,.08)}
.seller .title{margin-top:18px}
.seller .stock::before{content:"";display:inline-block;width:8px;height:8px;border-radius:50%;background:var(--green);margin-right:7px}
.footer{height:50px;background:var(--navy);display:flex;justify-content:center;align-items:center;gap:12px;color:var(--white);font-size:12px}
.pay{display:flex;justify-content:center;gap:7px;margin-top:32px}
.pay span,.ship span{height:24px;min-width:34px;padding:0 6px;background:var(--chip);font-size:11px;font-weight:600;color:var(--navy);display:flex;align-items:center}
.ship{display:flex;justify-content:center;margin-top:15px}
</style>
</head>
<body>
<div class="topbar">
  <span><svg width="18" height="12" viewBox="0 0 18 12"><rect x="1" y="1" width="16" height="10" fill="none" stroke="#fff" stroke-width="1.5"/><circle cx="9" cy="6" r="2.5" fill="#fff"/></svg>Gutscheincode "Plüsch" und 15% auf alle Kuschelbetten sichern</span>
  <span><svg width="18" height="18" viewBox="0 0 18 18"><path d="M9 1 16 5v8l-7 4-7-4V5z" fill="none" stroke="#fff" stroke-width="1.5"/><path d="M2 5l7 4 7-4M9 9v8" fill="none" stroke="#fff" stroke-width="1.5"/></svg>Kostenloser Versand ab €65,00</span>
</div>
<header class="header">
  <div class="brand"><i></i>Pfotenhain24</div>
  <div class="search">Suche</div>
  <div class="icons">
    <svg width="26" height="26" viewBox="0 0 26 26"><circle cx="13" cy="13" r="11.5" fill="none" stroke="#fff" stroke-width="2"/><circle cx="13" cy="10" r="4" fill="#fff"/><path d="M5.5 21c2-4 13-4 15 0" fill="#fff"/></svg>
    <svg width="30" height="26" viewBox="0 0 30 26"><path d="M2 9h26l-3 14H5z" fill="#fff"/><path d="M8 9l5-7M22 9l-5-7" stroke="#fff" stroke-width="2"/></svg>
    <div class="badge">0</div>
  </div>
</header>
<nav class="nav"><span>Pfotenhain24</span><span>Katzenkratzartikel</span><span>Plüschbetten</span><span>Katzenspielzeug</span><span>Interaktive Spielzeuge</span><span>Zubehör</span><span>SALE %</span><span>Kontakt</span></nav>
<section class="hero" role="img" aria-label="Foto: rote Katze liegt in einem Holzkatzenhaus auf einem Kissen, daneben Pflanzen in weißen Töpfen">
  <div class="dots"><i></i><i></i><i></i><i></i></div>
</section>
<section class="welcome">
  <svg width="100" height="110" viewBox="0 0 100 110" fill="var(--ink)"><ellipse cx="52" cy="74" rx="32" ry="28"/><ellipse cx="14" cy="50" rx="11" ry="15" transform="rotate(-25 14 50)"/><ellipse cx="38" cy="20" rx="12" ry="17" transform="rotate(-8 38 20)"/><ellipse cx="68" cy="22" rx="12" ry="17" transform="rotate(12 68 22)"/><ellipse cx="88" cy="52" rx="10" ry="14" transform="rotate(25 88 52)"/></svg>
  <h1>Willkommen bei Pfotenhain24.de</h1>
  <p>Hier findest Du eine liebevoll zusammengestellte Auswahl an Zubehör für deine vierbeinigen Familienmitglieder. Unsere Artikel wurden durch unser qualifiziertes, flauschiges Fachpersonal auf Haltbarkeit und Spielspaß geprüft und sind mit schnurrigen Grüßen zu empfehlen!</p>
</section>
<section class="offers">
  <h2>Top Angebote</h2>
  <div class="offer-row">
    <div class="offer"><div class="ph" role="img" aria-label="Foto: Katzen auf einer Kratzlounge" style="background:linear-gradient(#d8c6a8,#e8e4de 60%,#6a4a3a)"></div><div class="title">Kratzlounge L 580 x B 310 x H 300mm</div><div class="price">68,99 €</div><div class="stock">Auf Lager</div></div>
    <div class="offer"><div class="ph" role="img" aria-label="Foto: mehrfarbiges Plüsch-Kuschelbett" style="background:radial-gradient(#e6c7e0,#a9d3ea 60%,#d9d9d9)"></div><div class="title">Kuschelbett, mehrfarbig</div><div class="price">39,99 €</div><div class="stock opt">Optionen verfügbar</div></div>
    <div class="offer"><div class="ph" role="img" aria-label="Foto: Katze auf grüner Kratzpappe" style="background:linear-gradient(#dcdcdc,#c9c4b8 55%,#9fc760)"></div><div class="title">Footballfield Kratzpappe L 630 x B 350 x H 100mm</div><div class="price">55,99 €</div><div class="stock">Auf Lager</div></div>
    <div class="offer"><div class="ph" role="img" aria-label="Foto: Katze spielt mit interaktivem Spielzeug" style="background:linear-gradient(#7b7b7b,#b9b9b9 60%,#e9e9e9)"></div><div class="title">Schnurrtek Running Smart</div><div class="price">21,99 €</div><div class="stock">Auf Lager</div></div>
  </div>
</section>
<div class="rule"></div>
<section class="cats">
  <h2>Kategorien</h2>
  <div class="cat-row">
    <div class="cat" role="img" aria-label="Foto: weiße Katze auf Kratzsofa" style="background:linear-gradient(#0f5a4e,#1c6b5c 60%,#b58552)"><span>Katzenkratzartikel</span></div>
    <div class="cat" role="img" aria-label="Foto: Kätzchen im mintgrünen Plüschbett" style="background:radial-gradient(#dfe9e4,#9fcab6 70%)"><span>Plüschbetten</span></div>
    <div class="cat" role="img" aria-label="Foto: Kätzchen im Katzenlaufrad" style="background:linear-gradient(90deg,#c89a66,#d9e2ea 50%,#c99868)"><span>Katzenspielzeug</span></div>
  </div>
</section>
<section class="sellers">
  <h2>Top Seller</h2>
  <div class="seller-grid">
    <div class="seller"><div class="ph" role="img" aria-label="Foto: Katzen auf Kratzlounge" style="background:linear-gradient(#d8c6a8,#e8e4de 60%,#6a4a3a)"></div><div class="title">Kratzlounge L 580 x B 310 x H 300mm</div><div class="price">68,99 €</div><div class="stock">Auf Lager</div></div>
    <div class="seller"><div class="ph" role="img" aria-label="Foto: rosa Kratzsofa" style="background:linear-gradient(#c98a78,#e0a595 50%,#b97a68)"></div><div class="title">Kratzlounge L 580 x B 310 x H 300mm</div><div class="price">68,99 €</div><div class="stock">Auf Lager</div></div>
    <div class="seller"><div class="ph" role="img" aria-label="Foto: Fusselroller aus Holz" style="background:linear-gradient(#fff,#f3eadb 60%,#fff)"></div><div class="title">Kratzlounge L 580 x B 310 x H 300mm</div><div class="price">68,99 €</div><div class="stock">Auf Lager</div></div>
    <div class="seller"><div class="ph" role="img" aria-label="Foto: rote Spielzeugschlange auf Holzboden" style="background:linear-gradient(#f2d4cc,#d9b48d 55%,#c99a70)"></div><div class="title">Kratzlounge L 580 x B 310 x H 300mm</div><div class="price">68,99 €</div><div class="stock">Auf Lager</div></div>
    <div class="seller"><div class="ph" role="img" aria-label="Foto: Kratzball in Holzgestell" style="background:radial-gradient(#d3bf9c,#fff 70%)"></div><div class="title">Kratzlounge L 580 x B 310 x H 300mm</div><div class="price">68,99 €</div><div class="stock">Auf Lager</div></div>
    <div class="seller"><div class="ph" role="img" aria-label="Foto: bunte Plüschmäuse mit Katzenminze" style="background:linear-gradient(135deg,#4d7fd0,#e08a3c 50%,#7ab060)"></div><div class="title">Kratzlounge L 580 x B 310 x H 300mm</div><div class="price">68,99 €</div><div class="stock">Auf Lager</div></div>
  </div>
</section>
<footer class="footer"><span>Impressum</span><span>Datenschutz</span><span>Cookie-Richtlinie</span><span>Zahlung &amp; Versand</span><span>AGB</span><span>Widerrufsrecht</span></footer>
<div class="pay"><span>Karte</span><span>Kartix</span><span>Vesta</span><span>PayWell</span><span>Amerix</span><span>Ringcard</span></div>
<div class="ship"><span>Paketblitz</span></div>
</body>
</html>
```